Web Site for Strategy and Technology Consulting Company

We are looking for a website design that engages potential customers to understand our services and contact us. In this contest, we are looking for a homepage design, but the winning designer will be favored for the design of some of the more complicated interior pages of the site. An additional contest (or contests) for these pages will be added soon.

PLATROM AND RESPONSIVE DESIGN
The site will be implemented in WordPress using the Elementor page builder.
We are looking for a design that will look good on phones are well as laptop browsers.

UPLOADED FILES INCLUDE:
1a A wireframe of the homepage we are looking for. The Uploaded PDF also includes a draft of the text proposed for the homepage. Designers are free to go beyond the wireframe, but all elements of the wireframe should be included.
1b A Word document with the draft text of the homepage.
2a-d The Norvalith logo. Two versions are included – a dark version which works well against a light background, and a light version which works well against a dark background.
3 The Norvalith color palette with HEX and RGB values. Designers are not limited to this palette, but colors should be complementary.
4 A draft of the homepage menu
5 Service sheets with information on the services we provide

MORE ABOUT NORVALITH
Norvalith is a consulting company focused on transforming businesses through software. Our tagline, “Transformation Delivered,” recognizes the gap business often have between business transformation and the software they end up with. By listening to our customers and understanding their vision and where they are, we help get our customers where they want to go.

We increase our capability by working with many consultants and partners, allowing us to provide our customers with the best people and the software that best suits them.

Industry/Entity Type

Consulting

Number of Pages Required

1 page

Font styles to use
Sans Serif

Requirements
Must have
• the content represented on the wireframe uploaded
Nice to have
• interactive features, such as roll-over icons that reveal additional information

```html
<!DOCTYPE html>
<html lang="en">
<head>
<meta charset="utf-8">
<title>Norvalith — Transformation Delivered</title>
<link rel="stylesheet" href="https://fonts.googleapis.com/css2?family=Ubuntu:wght@400;500;700&display=swap">
<style>
:root{
  --brand-blue:#2a5d8f;
  --brand-gold:#d9b51c;
  --slate:#44546c;
  --ink:#1d1d1d;
  --grey-card:#e6e6e6;
  --logo-grey:#8a8f99;
  --white:#ffffff;
  --footer-blue:#3a77ab;
}
*{box-sizing:border-box;margin:0;padding:0}
html,body{width:1200px;height:3145px;overflow:hidden}
body{position:relative;font-family:"Ubuntu",sans-serif;color:var(--ink);
  background:linear-gradient(180deg,#fff 0,#fff 2470px,#b9cde0 2680px,#6d9bc4 2880px,var(--footer-blue) 3145px)}
.abs{position:absolute}
.btn{position:absolute;display:flex;align-items:center;justify-content:center;color:#fff;font-weight:500;font-size:20px;
  border-radius:6px;background:linear-gradient(90deg,var(--brand-blue),var(--brand-gold));text-decoration:none}

/* header */
.site-header{left:0;top:0;width:1200px;height:90px;background:#fff;border-top:5px solid var(--brand-blue)}
.logo{display:flex;align-items:center;gap:8px;font-weight:400}
.logo-mark{width:14px;height:14px;background:var(--brand-blue)}
.header-logo{left:99px;top:17px;font-size:44px;color:var(--logo-grey)}
.main-nav a{position:absolute;top:26px;font-size:17px;color:var(--ink);text-decoration:none}
.contact-btn{left:934px;top:19px;width:167px;height:43px}

/* hero */
.hero-photo{left:0;top:90px;width:1200px;height:580px;
  background:linear-gradient(90deg,#5d5f63 0%,#8b8c8e 35%,#c9c2b8 55%,#e8ded2 75%,#cfd3d6 100%)}
.hero-shade{left:0;top:90px;width:720px;height:580px;background:linear-gradient(90deg,rgba(40,40,45,.55),rgba(40,40,45,0))}
.hero-title{left:99px;top:188px;font-size:35px;font-weight:700;color:#fff;letter-spacing:.3px}
.hero-lead{left:99px;top:246px;width:610px;font-size:16px;line-height:26px;font-weight:500;color:#fff}
.bullets{list-style:none}
.bullets li{position:relative;padding-left:22px;color:#fff}
.bullets li::before{content:"";position:absolute;left:2px;top:8px;border-left:6px solid var(--brand-gold);border-top:4px solid transparent;border-bottom:4px solid transparent}
.hero-bullets{left:99px;top:366px;width:520px;font-size:15px;line-height:26px}
.story-btn{left:99px;top:516px;width:167px;height:43px}

/* tech section */
.section-title{left:0;width:1200px;text-align:center;font-size:34px;font-weight:500;color:var(--brand-blue)}
.tech-intro{left:171px;top:818px;width:858px;text-align:center;font-size:17px;line-height:26px;color:#333}
.how-btn{left:516px;top:933px;width:207px;height:45px}
.service-card{top:1046px;width:238px}
.service-card .head{height:156px;background:var(--grey-card);border-radius:4px;text-align:center;padding-top:36px;font-weight:700;font-size:21px;line-height:26px}
.service-card .icon{position:absolute;left:68px;top:107px;width:102px;height:102px;border-radius:50%;background:var(--brand-blue);border:3px solid var(--brand-gold);display:flex;align-items:center;justify-content:center}
.service-card p{position:absolute;top:226px;left:14px;width:210px;text-align:center;font-size:21px;line-height:31px}
.arrow{width:20px;height:20px}

/* people */
.people-band{left:0;top:1471px;width:1200px;height:593px;background:var(--slate)}
.people-title{left:99px;top:1528px;font-size:35px;font-weight:500;color:#fff}
.people-text{left:99px;top:1592px;width:540px;font-size:15px;line-height:29px;font-weight:700;color:#fff}
.people-bullets{left:106px;top:1729px;width:540px;font-size:13px;line-height:29px}
.people-close{left:99px;top:1833px;width:540px;font-size:15px;line-height:29px;font-weight:700;color:#fff}
.team-btn{left:99px;top:1929px;width:167px;height:46px}
.people-photo{left:689px;top:1536px;width:407px;height:439px;border-radius:8px;
  background:linear-gradient(160deg,#7d8f9b 0%,#c4b39a 55%,#b58b52 100%)}

/* testimonials */
.testimonial{top:2263px;width:481px;height:169px;border:2px solid #ddd;border-radius:85px}
.avatar{position:absolute;left:-2px;top:2px;width:161px;height:161px;border-radius:50%;border:7px solid}
.testimonial .name{position:absolute;left:182px;top:26px;font-size:19px}
.testimonial .role{position:absolute;left:182px;top:54px;font-size:14px}
.testimonial .quote{position:absolute;left:182px;top:86px;width:260px;font-size:10.5px;line-height:15px}

/* technologies */
.tech-tile{top:2638px;width:226px;height:94px;background:#fff;border-radius:4px;display:flex;align-items:center;justify-content:center;font-size:30px}

/* footer */
.footer-logo{left:0;width:1200px;top:2826px;justify-content:center;font-size:72px;color:#fff;font-weight:500}
.footer-logo .logo-mark{background:#fff}
.footer-nav a{position:absolute;top:2932px;font-size:17px;color:#fff;text-decoration:none}
.social{top:2981px;width:39px;height:39px;border-radius:50%;border:2px solid var(--brand-gold);background:var(--brand-blue)}
.footer-rule{left:101px;top:3041px;width:999px;height:1px;background:rgba(255,255,255,.6)}
.copyright{left:0;width:1200px;top:3066px;text-align:center;color:#fff;font-size:15px}
</style>
</head>
<body>

<header class="abs site-header">
  <div class="abs logo header-logo"><span class="logo-mark"></span>Norvalith</div>
  <nav class="main-nav">
    <a style="left:398px">About Us</a>
    <a style="left:537px">Services</a>
    <a style="left:669px">Insights</a>
    <a style="left:797px">Join Us</a>
  </nav>
  <a class="btn contact-btn">Contact Us</a>
</header>

<section class="hero">
  <div class="abs hero-photo" role="img" aria-label="Photo of two smiling colleagues reviewing a document in an office"></div>
  <div class="abs hero-shade"></div>
  <h1 class="abs hero-title">TRANSFORMATION DELIVERED</h1>
  <p class="abs hero-lead">We do more for our customers than implement software. We listen. We work to understand where they are in their transformation journey and where they want to go. We partner with them to clear the roadblocks that stand in their way, ensuring they reach their destination. At Norvalith, we:</p>
  <ul class="abs bullets hero-bullets">
    <li>Focus on business value, with an emphasis on delivering value quickly.</li>
    <li>Meet our customers where they are without backing them up to the beginning of their journey.</li>
    <li>Provide a wide range of services, from strategy to product support.</li>
    <li>Commit to our customer’s long-term success.</li>
  </ul>
  <a class="btn story-btn">Our Story</a>
</section>

<section class="technology">
  <h2 class="abs section-title" style="top:756px">TRANSFORMATION SUPPORTED BY TECHNOLOGY</h2>
  <p class="abs tech-intro">During our early years, Norvalith focused only on business transformation. We came to realize that successful transformation often depended on quality software implementations, and often more than one. Now we focus on five things, the five things most businesses need to reach their goals.</p>
  <a class="btn how-btn">How We Work</a>

  <svg class="abs arrow" style="left:44px;top:1188px" viewBox="0 0 20 20"><circle cx="10" cy="10" r="10" fill="#2a5d8f"/><path d="M12 5 7 10l5 5" stroke="#fff" stroke-width="2.5" fill="none"/></svg>
  <svg class="abs arrow" style="left:1127px;top:1188px" viewBox="0 0 20 20"><circle cx="10" cy="10" r="10" fill="#2a5d8f"/><path d="M8 5l5 5-5 5" stroke="#fff" stroke-width="2.5" fill="none"/></svg>

  <div class="abs service-card" style="left:99px">
    <div class="head">Business<br>Transformation</div>
    <div class="icon"><svg width="46" height="52" viewBox="0 0 46 52" fill="none" stroke="#fff" stroke-width="2"><rect x="4" y="6" width="38" height="44" rx="2"/><rect x="15" y="2" width="16" height="8"/><circle cx="14" cy="40" r="3"/><circle cx="30" cy="22" r="3"/><path d="M16 37l12-13M30 38l4 4M34 38l-4 4"/></svg></div>
    <p>Define and execute your strategy.</p>
  </div>
  <div class="abs service-card" style="left:353px">
    <div class="head">ERP<br>Implementations</div>
    <div class="icon"><svg width="54" height="46" viewBox="0 0 54 46" fill="none" stroke="#fff" stroke-width="2"><rect x="2" y="2" width="50" height="32" rx="2"/><path d="M20 34v8M34 34v8M14 42h26M8 26h38M10 22l8-8 6 5 8-9 8 6"/></svg></div>
    <p>Assess, upgrade, and implement ERP solutions to meet your needs</p>
  </div>
  <div class="abs service-card" style="left:608px">
    <div class="head">CRM<br>Implementations</div>
    <div class="icon"><svg width="56" height="52" viewBox="0 0 56 52" fill="none" stroke="#fff" stroke-width="2"><circle cx="14" cy="12" r="8"/><circle cx="14" cy="38" r="8"/><circle cx="14" cy="38" r="3"/><rect x="30" y="4" width="22" height="18"/><rect x="30" y="28" width="22" height="18"/><path d="M34 10h14M34 16h14M36 32v10M41 32v10M46 32v10M22 12h8M22 38h8"/></svg></div>
    <p>Take your relationships to the next level.</p>
  </div>
  <div class="abs service-card" style="left:862px">
    <div class="head">BI and Data</div>
    <div class="icon"><svg width="54" height="46" viewBox="0 0 54 46" fill="none" stroke="#fff" stroke-width="2"><rect x="2" y="2" width="50" height="30" rx="2"/><path d="M27 32v8M16 42h22M10 22h34M10 14v6M14 10v10M18 14v6"/><circle cx="38" cy="13" r="6"/><path d="M38 7v6h6"/></svg></div>
    <p>Discover, connect, and trust your data.</p>
  </div>
</section>

<section class="people">
  <div class="abs people-band"></div>
  <h2 class="abs people-title">IT’S THE PEOPLE</h2>
  <p class="abs people-text">The world has changed in the past twenty years. The people you need might not all work for one company. Our clients want the best resources, available quickly. That’s why, in addition to our team of experts, we partner with:</p>
  <ul class="abs bullets people-bullets">
    <li>A large network of expert consultants who are the best at what they do,</li>
    <li>Service providers all over the world to provide the resources and value that are right for you, available 24 x 7.</li>
  </ul>
  <p class="abs people-close">People are invariably at the center of our customer’s success. Find out how we can add our experts to yours.</p>
  <a class="btn team-btn">Our Team</a>
  <div class="abs people-photo" role="img" aria-label="Photo of a smiling consultant in glasses working at a laptop"></div>
</section>

<section class="testimonials">
  <h2 class="abs section-title" style="top:2176px">TESTIMONIALS</h2>
  <div class="abs testimonial" style="left:101px">
    <div class="avatar" role="img" aria-label="Portrait of a client on the phone" style="border-color:var(--brand-gold);background:linear-gradient(160deg,#a9b4c0,#3c4a5c)"></div>
    <div class="name">Lorem ipsum</div>
    <div class="role">Designer</div>
    <p class="quote">Sed ut perspiciatis unde omnis iste natus error sit voluptatem accusantium doloremque laudantium, totam rem aperiam, eaque ipsa quae ab illo</p>
  </div>
  <div class="abs testimonial" style="left:621px">
    <div class="avatar" role="img" aria-label="Portrait of a smiling client" style="border-color:var(--brand-blue);background:linear-gradient(160deg,#8c8f95,#4b3a30)"></div>
    <div class="name">Lorem ipsum</div>
    <div class="role">Designer</div>
    <p class="quote">Sed ut perspiciatis unde omnis iste natus error sit voluptatem accusantium doloremque laudantium, totam rem aperiam, eaque ipsa quae ab illo</p>
  </div>
</section>

<section class="technologies">
  <h2 class="abs section-title" style="top:2542px">TECHNOLOGIES</h2>
  <svg class="abs arrow" style="left:55px;top:2676px" viewBox="0 0 20 20"><circle cx="10" cy="10" r="10" fill="#2a5d8f"/><path d="M12 5 7 10l5 5" stroke="#fff" stroke-width="2.5" fill="none"/></svg>
  <svg class="abs arrow" style="left:1116px;top:2676px" viewBox="0 0 20 20"><circle cx="10" cy="10" r="10" fill="#2a5d8f"/><path d="M8 5l5 5-5 5" stroke="#fff" stroke-width="2.5" fill="none"/></svg>
  <div class="abs tech-tile" style="left:99px;color:#d9b51c">Vistachart</div>
  <div class="abs tech-tile" style="left:356px;color:#c0322a;font-size:24px">Ledgerline Insight</div>
  <div class="abs tech-tile" style="left:612px;color:#555a5e;font-weight:700">Quorra</div>
  <div class="abs tech-tile" style="left:869px;color:#3aa8dc">Frostbase</div>
</section>

<footer>
  <div class="abs logo footer-logo"><span class="logo-mark"></span>Norvalith</div>
  <nav class="footer-nav">
    <a style="left:370px">About Us</a>
    <a style="left:509px">Services</a>
    <a style="left:640px">Insights</a>
    <a style="left:768px">Join Us</a>
  </nav>
  <div class="abs social" style="left:528px"></div>
  <div class="abs social" style="left:580px"></div>
  <div class="abs social" style="left:633px"></div>
  <div class="abs footer-rule"></div>
  <p class="abs copyright">Copyright ©2023 Norvalith&nbsp; All Rights Reserved</p>
</footer>

</body>
</html>
```